Halvard Property Website

Our organization has multiple arms. We want a 5-page website to address the divisions of our company. Pelgrave Yards, our 1500 square foot flex office space will have 3 of those pages. We need a landing page for Halvard Property Holdings and a Contact Us page for the organization. Then the 3 pages dedicated to Pelgrave Yards: a page showing office pictures, a page for pricing, and a calendar page for this part of our business; for a total of 5 pages.
Updates

Please note, we need a logo for Pelgrave Yards (the flex office space). We have a logo for Halvard Property (see attachments). It is not a requirement for Pelgrave's logo to match Halvard's logo.

Industry/Entity Type

Real Estate

Coding

Requirements
Must have
• Domain, Email, Logo (for Pelgrave Yards),

```html
<!DOCTYPE html>
<html lang="en">
<head>
<meta charset="utf-8">
<title>Halvard Property Holdings</title>
<link href="https://fonts.googleapis.com/css2?family=Tinos:wght@700&family=PT+Sans:wght@400;700&display=swap" rel="stylesheet">
<style>
:root{
  --pink:#e8336f;
  --berry:#b01147;
  --navy:#17324a;
  --gold:#fdc300;
  --ink:#1b1b1b;
  --dark:#1e1c1d;
  --grey:#a9a9ab;
  --field:#f3f3f3;
}
*{box-sizing:border-box;margin:0;padding:0}
html,body{width:1200px;height:2603px;overflow:hidden;background:#fff}
body{position:relative;font-family:"PT Sans",sans-serif;color:var(--ink)}
.abs{position:absolute}
.serif{font-family:"Tinos",serif;font-weight:700}
.btn{position:absolute;background:var(--gold);border-radius:22px;font-weight:700;color:var(--ink);display:flex;align-items:center;justify-content:center}
.dot{display:inline-block;width:16px;height:16px;border-radius:50%;background:var(--pink);margin-right:10px;vertical-align:middle}
/* header */
.follow{left:142px;top:42px;font-size:16px;font-weight:700;color:var(--pink)}
.brand{left:0;width:1200px;top:34px;text-align:center;font-size:28px;letter-spacing:3px;color:var(--ink)}
.nav{left:0;top:99px;width:1200px;height:40px;background:var(--pink);display:flex;justify-content:center;gap:48px;align-items:center;font-size:17px;color:#fff}
.nav .on{color:var(--ink);font-weight:700}
.hero{left:0;top:139px;width:1200px;height:562px;background:linear-gradient(100deg,#14304a 0%,#1b3a56 50%,#2a3f55 75%,#3b4a5c 100%)}
.hero-photo{left:540px;top:139px;width:660px;height:562px;background:radial-gradient(ellipse at 55% 55%,rgba(214,160,130,.55),rgba(60,80,100,.2) 55%,transparent 75%)}
/* pricing */
.card{position:absolute;background:#fff;border-radius:14px;box-shadow:0 0 6px rgba(0,0,0,.12);text-align:center}
.card h3{font-family:"Tinos",serif;color:var(--berry);font-size:22px}
.card .price{font-weight:700;font-size:46px;color:#000}
.rows{position:absolute;font-size:17px;line-height:27px;text-align:left}
.enroll{position:absolute;width:122px;height:30px;border-radius:15px;font-size:14px;display:flex;align-items:center;justify-content:center;box-shadow:0 1px 4px rgba(0,0,0,.25)}
/* contact */
.field{position:absolute;background:var(--field);border-radius:10px;padding:20px 21px;font-size:17px;color:#777}
.fnav{left:0;top:2431px;width:1200px;height:46px;background:var(--grey);display:flex;justify-content:center;gap:35px;align-items:center;font-size:15px;color:var(--ink)}
.info{top:2498px;font-size:14px;display:flex;align-items:center;gap:8px}
</style>
</head>
<body>

<!-- header -->
<div class="abs follow">Follow us : <span class="dot" style="margin-left:8px"></span><span class="dot"></span><span class="dot"></span></div>
<div class="abs brand serif">HALVARD PROPERTY HOLDINGS</div>
<svg class="abs" style="left:1022px;top:34px" width="36" height="36" viewBox="0 0 36 36" aria-label="Calendar">
  <rect x="2" y="5" width="32" height="29" rx="3" fill="#f1f1f1" stroke="#ccc"/>
  <rect x="2" y="5" width="32" height="9" rx="3" fill="#e23b3b"/>
  <rect x="9" y="1" width="3" height="8" fill="#777"/><rect x="24" y="1" width="3" height="8" fill="#777"/>
  <text x="18" y="30" font-size="15" text-anchor="middle" fill="#333" font-family="PT Sans,sans-serif" font-weight="700">31</text>
</svg>
<nav class="abs nav"><span class="on">Home</span><span>About</span><span>Services</span><span>Contact</span></nav>

<!-- hero -->
<div class="abs hero"></div>
<div class="abs hero-photo" role="img" aria-label="Businessman in a suit holding a model house on his open hand"></div>
<div class="abs serif" style="left:143px;top:270px;font-size:27px;color:#fff">Welcome to</div>
<div class="abs serif" style="left:141px;top:300px;font-size:88px;line-height:96px;color:#fff">HALVARD</div>
<div class="abs serif" style="left:143px;top:390px;font-size:37px;color:#fff">Real Estate Enterprise</div>
<p class="abs" style="left:143px;top:453px;width:360px;font-size:17px;line-height:27px;color:#fff">Lorem Ipsum is simply dummy text of the printing and typesetting industry.</p>
<div class="btn" style="left:143px;top:528px;width:147px;height:40px;font-size:17px">Get Started</div>

<!-- about -->
<h2 class="abs serif" style="left:143px;top:756px;font-size:38px;color:var(--navy)">About Us</h2>
<p class="abs" style="left:143px;top:826px;width:550px;font-size:16.5px;line-height:27px">Lorem Ipsum is simply dummy text of the printing and typesetting industry. Lorem Ipsum has been the industry's standard dummy text ever since the 1500s, when an unknown printer took a galley of type and scrambled it to make a type specimen book. It has survived not only five centuries, but also the leap into electronic typesetting, remaining essentially unchanged. It was popularised in the 1960s with the release of Letraset sheets ldus PageMaker including versions of Lorem Ipsum.</p>
<div class="btn" style="left:143px;top:1043px;width:147px;height:40px;font-size:17px">Read More</div>
<div class="abs" role="img" aria-label="Businessman steadying a model house on a tower of wooden blocks" style="left:730px;top:773px;width:374px;height:332px;border-radius:4px;background:linear-gradient(120deg,#b9c0c8,#8d96a0 45%,#c9a77f 70%,#9aa3ad)"></div>

<!-- pricing -->
<svg class="abs" style="left:0;top:1217px" width="1200" height="270" viewBox="0 0 1200 270">
  <path d="M0 0H1200V130C1000 230 780 262 600 262C420 262 200 230 0 128Z" fill="var(--berry)"/>
</svg>
<h2 class="abs serif" style="left:0;width:1200px;top:1228px;text-align:center;font-size:52px;color:#fff">Pricing</h2>

<div class="card" style="left:181px;top:1342px;width:246px;height:344px">
  <h3 style="margin-top:27px">Commercial</h3>
  <div class="price" style="margin-top:8px">$1,000</div>
  <div class="rows" style="left:42px;top:142px">Sample<br>Sample<br>Sample<br>Sample</div>
  <div class="rows" style="left:145px;top:144px;font-size:15px">$185<br>$350<br>$350<br>$515</div>
  <div class="enroll" style="left:47px;top:278px;background:var(--gold)">Enroll Now</div>
</div>
<div class="card" style="left:457px;top:1307px;width:281px;height:390px;border:2px solid var(--pink)">
  <h3 style="margin-top:28px">Residential</h3>
  <div class="price" style="margin-top:8px;font-size:50px">$1,500</div>
  <div class="rows" style="left:53px;top:162px;line-height:32px">Sample<br>Sample<br>Sample<br>Sample</div>
  <div class="rows" style="left:180px;top:162px;line-height:32px;font-size:15px">$130<br>$240<br>$240<br>$405</div>
  <div class="enroll" style="left:74px;top:310px;background:#fff">Enroll Now</div>
</div>
<div class="card" style="left:784px;top:1342px;width:246px;height:344px">
  <h3 style="margin-top:21px">Commercial Showroom</h3>
  <div class="price" style="margin-top:14px">$5,000</div>
  <div class="rows" style="left:35px;top:142px">Sample<br>Sample<br>Sample<br>Sample</div>
  <div class="rows" style="left:160px;top:144px;font-size:15px">$103<br>$185<br>$185<br>$295</div>
  <div class="enroll" style="left:57px;top:274px;background:var(--gold)">Enroll Now</div>
</div>

<!-- contact -->
<div class="abs" role="img" aria-label="Dotted world map backdrop" style="left:0;top:1793px;width:1200px;height:502px;background:radial-gradient(ellipse at 50% 45%,#2e2c2d,var(--dark) 70%)"></div>
<h2 class="abs serif" style="left:0;width:1200px;top:1840px;text-align:center;font-size:52px;color:#fff">Contact us</h2>
<div class="field" style="left:214px;top:1932px;width:376px;height:64px">Name</div>
<div class="field" style="left:214px;top:2013px;width:376px;height:64px">Email</div>
<div class="field" style="left:214px;top:2095px;width:376px;height:63px">Phone</div>
<div class="field" style="left:610px;top:1932px;width:376px;height:224px">Message</div>
<div class="btn" style="left:526px;top:2193px;width:148px;height:40px;font-size:17px">Submit</div>

<!-- footer -->
<div class="abs serif" style="left:143px;top:2354px;font-size:22px;letter-spacing:2px"><span class="abs" style="left:0;top:4px;width:22px;height:22px;background:var(--pink)"></span><span style="margin-left:32px">HALVARD</span></div>
<div class="abs serif" style="left:392px;top:2354px;font-size:22px;letter-spacing:2px"><span class="abs" style="left:0;top:4px;width:22px;height:22px;border-radius:50%;background:var(--pink)"></span><span style="margin-left:32px">PELGRAVE YARDS</span></div>
<p class="abs" style="left:655px;top:2340px;width:405px;font-size:14px;line-height:27px;color:#444;text-align:justify">Lorem Ipsum is simply dummy text of the printing and typesetting industry. Lorem Ipsum has standard dummy text ever since the 1500s.</p>

<nav class="abs fnav"><span>HOME</span><span>About Us</span><span>Services</span><span>Pricing</span><span>Contact Us</span></nav>

<div class="abs info" style="left:336px">
  <svg width="15" height="15" viewBox="0 0 24 24"><path d="M6 2l4 4-2.5 2.5a14 14 0 0 0 8 8L18 14l4 4-3 3C10 21 3 14 3 5z" fill="none" stroke="#222" stroke-width="2"/></svg>(555) 014 2290</div>
<div class="abs info" style="left:518px">
  <svg width="13" height="10" viewBox="0 0 13 10"><rect width="13" height="10" fill="#222"/><path d="M0 0l6.5 5L13 0" stroke="#fff" fill="none"/></svg>hello@halvardproperty.com</div>
<div class="abs info" style="left:723px">
  <svg width="10" height="14" viewBox="0 0 10 14"><path d="M5 0a5 5 0 0 1 5 5c0 4-5 9-5 9S0 9 0 5a5 5 0 0 1 5-5z" fill="#222"/><circle cx="5" cy="5" r="2" fill="#fff"/></svg>48 Linden Row, USA 20415</div>
<div class="abs" style="left:0;top:2541px;width:1200px;height:1px;background:#ddd"></div>

<div class="abs" style="left:143px;top:2561px"><span class="dot" style="background:#222;margin-right:18px"></span><span class="dot" style="background:#222;margin-right:18px"></span><span class="dot" style="background:#222"></span></div>
<div class="abs" style="left:731px;top:2561px;font-size:13px">© copyrights 2022 Halvard Property | &nbsp;All Rights Reserved</div>

</body>
</html>
```